Visitenkarten-Design für Immobilienfinanzierer
Zielgruppe
Ich bin hauptsächlich Immobilienfinanzierer. Das bedeutet, dass ich als unabhängiger Finanzmakler für meine Kunden aus über 400 Banken, Versicherungsgesellschaften und Bausparkassen den Finanzierungspartner auswähle, der die beste Kondition anbietet, oder das Projekt überhaupt begleitet. Die durch die Baufinanzierung gewonnenen Kunden berate ich auch zu den Themen Bausparen, Versicherungen, Vermögensanlagen und Privatkredite. Kernthema mit 80% Umsatzanteil ist die Bau/Immobilienfinanzierung. Mitbewerber mit ähnlichem Geschäftsmodell sind hauptsächlich Dr. Wendau, Baveron.
Aufgabenstellung
In meiner Branche ist Seriosität das Maß aller Dinge. Dabei möchte ich eher modern als altbacken auftreten (kein 'Kanzlei'-Design', aber auch nicht zu flippig. Ich bin 40 Jahre alt, und möchte auch mit 60 noch zum Design passen.

```html
<!DOCTYPE html>
<html lang="de">
<head>
<meta charset="utf-8">
<title>Visitenkarte – velora private finance</title>
<link href="https://fonts.googleapis.com/css2?family=Open+Sans:wght@400;600&display=swap" rel="stylesheet">
<style>
  :root {
    --stage: #1f1f20;
    --card-white: #ffffff;
    --card-dark: #4a4a4a;
    --band-dark: #3e3e3e;
    --ink: #3a3a3a;
    --ink-soft: #6a6a6a;
    --green: #95c23d;
    --grey-light: #9a9a9a;
    --icon: #8c8c8c;
  }
  * { margin: 0; padding: 0; box-sizing: border-box; }
  html, body {
    width: 1200px; height: 801px; overflow: hidden;
    background: var(--stage);
    font-family: "Open Sans", sans-serif;
  }
  .stage {
    width: 1200px; height: 801px;
    display: flex; align-items: center; justify-content: center; gap: 50px;
  }
  .card {
    width: 500px; height: 320px; position: relative; overflow: hidden;
    border-radius: 4px;
  }
  /* Front */
  .card--front { background: var(--card-white); color: var(--ink); }
  .person { position: absolute; left: 56px; top: 52px; }
  .person__name { font-size: 21px; font-weight: 400; letter-spacing: -0.2px; line-height: 1; }
  .person__role { font-size: 7.5px; letter-spacing: 1.3px; color: var(--ink-soft); margin-top: 4px; }
  .contact { position: absolute; left: 56px; top: 118px; font-size: 11.5px; line-height: 17px; }
  .contact__title { font-size: 13px; margin-bottom: 5px; }
  .contact__key { color: var(--green); display: inline-block; width: 16px; }
  .accent-bar {
    position: absolute; left: 22px; top: 172px; width: 22px; height: 52px;
    background: var(--green);
  }
  .address { position: absolute; left: 56px; top: 240px; font-size: 11.5px; line-height: 17px; }
  .address__title { color: var(--green); font-size: 13px; }
  .brand-mark { position: absolute; right: 48px; top: 42px; }
  /* Back */
  .card--back { background: var(--card-dark); }
  .brand {
    position: absolute; left: 0; right: 0; top: 96px;
    display: flex; align-items: center; justify-content: center; gap: 16px;
  }
  .brand__name {
    font-size: 40px; font-weight: 400; color: var(--grey-light);
    line-height: 1.05; letter-spacing: 0.5px;
  }
  .band {
    position: absolute; left: 0; right: 0; bottom: 0; height: 92px;
    background: var(--band-dark); border-radius: 0 22px 0 0;
  }
  .social { position: absolute; right: 26px; top: 14px; display: flex; gap: 8px; }
  .social__item { width: 20px; height: 20px; background: var(--icon); border-radius: 3px; }
  .band__web {
    position: absolute; left: 28px; bottom: 16px;
    font-size: 12px; color: var(--grey-light); letter-spacing: 0.4px;
  }
</style>
</head>
<body>
<main class="stage">
  <section class="card card--front" aria-label="Vorderseite">
    <div class="person">
      <p class="person__name">Marlene Vossberg</p>
      <p class="person__role">IMMOBILIENFINANZIERER</p>
    </div>
    <div class="contact">
      <p class="contact__title">Kontakt</p>
      <p><span class="contact__key">T.</span>+49 00 00000 00</p>
      <p><span class="contact__key">F.</span>+49 00 00000 00</p>
      <p><span class="contact__key">E.</span>info@veloraprivatefinance</p>
      <p><span class="contact__key">W.</span>www.veloraprivatefinance</p>
    </div>
    <div class="accent-bar"></div>
    <div class="address">
      <p class="address__title">Immobilienfinanzierer</p>
      <p>Südliche Parkstr. 22 B</p>
      <p>D-81475 Lindenhain</p>
    </div>
    <svg class="brand-mark" width="130" height="130" viewBox="0 0 130 130" aria-hidden="true">
      <circle cx="65" cy="65" r="52" fill="none" stroke="var(--green)" stroke-width="14"/>
    </svg>
  </section>

  <section class="card card--back" aria-label="Rückseite">
    <div class="brand">
      <svg width="56" height="56" viewBox="0 0 56 56" aria-hidden="true">
        <circle cx="28" cy="28" r="22" fill="none" stroke="var(--grey-light)" stroke-width="7"/>
      </svg>
      <p class="brand__name">velora<br>private finance</p>
    </div>
    <div class="band">
      <div class="social">
        <span class="social__item"></span>
        <span class="social__item"></span>
        <span class="social__item"></span>
      </div>
      <p class="band__web">www.baufinanzkompass.de</p>
    </div>
  </section>
</main>
</body>
</html>
```